Post Card Mailer for QUIK PATH PROSPECTS using new logo

We need a post card designed to send through the USA mail service that will go to new prospective clients.

The post card will introduce me and my new company and try to educate them our on company and services.

The goal is for them to call me or email me so I can have a discussion and try to sell our product.

Our product is a name list of individuals that are looking for consulting / help to determine if they qualify for USA social security benefits and then help to manage the process. We sell this name list to law firms that help these individuals.

Our services are better because we have a better less expensive way to identify people via the internet that want help. Our conversion rate is 15%, so every 100 leads a law firm buys the will obtain 15 customers / clients.

Designer on Logo took alot longer than expected. Also there were two projects that needed to combined into one. Which was done yesterday.

Target Market(s)

Law firms

Font styles to use
Serif
Sans Serif
Script

Colors

Designer to choose colors to be used in the design.

Requirements
Must have
• The size of the mailer should be about 6 by 8 inches.
• Two sides.
• Side 1: With our Logo and key messages we want to communicate.
• Side 2: A space to be used by the USA mail services in lower right, my photo and an introduction by me to our company and why they should buy from my company.
Nice to have
• Images that represent what we do, how we help, and our target market.
Should not have
• Poor taste in images that upset people

```html
<!DOCTYPE html>
<html lang="en">
<head>
<meta charset="utf-8">
<title>Quik Path Prospects – Post Card Mailer</title>
<link rel="stylesheet" href="https://fonts.googleapis.com/css2?family=Montserrat+Alternates:wght@500;600;700&family=Quicksand:wght@400;500;600;700&family=Ubuntu+Condensed&display=swap">
<style>
:root{
  --stage:#d6d6d6;
  --navy:#0b2f4e;
  --deep:#0f4d84;
  --blue:#1a74c2;
  --bright:#2d95e0;
  --glow:#55b4f0;
  --ink:#0d4f7e;
  --grey:#8a8f94;
  --white:#ffffff;
}
*{margin:0;padding:0;box-sizing:border-box}
html,body{width:774px;height:1200px;overflow:hidden;background:var(--stage)}
.card{position:absolute;left:62px;width:644px;overflow:hidden}
.card-front{top:75px;height:482px;background:linear-gradient(180deg,var(--navy) 0%,var(--deep) 45%,var(--blue) 100%)}
.card-back{top:624px;height:488px;background:var(--white)}
.front-art,.back-art{position:absolute;inset:0}
.brand{position:absolute;left:0;right:0;top:78px;text-align:center;font-family:"Montserrat Alternates",sans-serif;font-weight:700;font-size:33px;letter-spacing:2px;color:#3f9ce0}
.pill{position:absolute;height:66px;border-radius:34px;background:linear-gradient(180deg,var(--bright),var(--blue));border:2px solid var(--glow);box-shadow:0 3px 8px rgba(0,20,50,.35);color:var(--white);font-family:"Ubuntu Condensed",sans-serif}
.pill-icon{position:absolute;left:8px;top:9px;width:44px;height:44px;border-radius:50%;background:radial-gradient(circle,#1f80cc,#12558f);border:2px solid var(--glow)}
.pill-mark{display:flex;align-items:center;justify-content:center;font-size:7px;letter-spacing:.5px;text-align:center}
.pill h3{position:absolute;left:72px;top:6px;font-weight:400;font-size:14px;padding-bottom:2px;border-bottom:1px solid var(--white);white-space:nowrap}
.pill ul{position:absolute;left:72px;top:30px;list-style:none;font-size:10px;line-height:16px;white-space:nowrap}
.pill li::before{content:"";display:inline-block;width:4px;height:4px;background:var(--white);margin:0 9px 2px 0;vertical-align:middle}
.back-name{position:absolute;left:173px;top:56px;font-family:"Montserrat Alternates",sans-serif;font-weight:600;font-size:29px;color:var(--white);white-space:nowrap}
.back-role{position:absolute;left:174px;top:100px;font-family:"Quicksand",sans-serif;font-weight:600;font-size:10px;color:var(--white)}
.back-brand{position:absolute;left:430px;top:34px;width:180px;text-align:center;font-family:"Montserrat Alternates",sans-serif;font-weight:700;font-size:19px;line-height:24px;letter-spacing:1px;color:#3f9ce0}
.tagline{position:absolute;left:174px;top:127px;font-family:"Quicksand",sans-serif;font-weight:700;font-size:11.5px;line-height:14px;color:var(--ink);white-space:nowrap}
.copy{position:absolute;font-family:"Quicksand",sans-serif;color:var(--ink);white-space:nowrap}
.copy h2{font-weight:600;font-size:16px}
.copy h4{font-weight:700;font-size:12.5px;display:inline-block;border-bottom:1px solid var(--ink);padding-bottom:2px}
.copy ul{list-style:none;font-size:10.5px;font-weight:500;color:#2f7fb8}
.copy li::before{content:"";display:inline-block;width:4px;height:4px;background:var(--ink);margin:0 8px 2px 0;vertical-align:middle}
.test{left:100px;top:184px}
.test ul{margin:6px 0 0 4px;line-height:16px}
.intro{left:84px;top:254px;width:320px}
.intro ul{margin:8px 0 0 0;line-height:17.5px}
.intro h5{font-size:12px;font-weight:700;margin-top:3px}
.intro h5::before{content:"";display:inline-block;width:4px;height:4px;background:var(--ink);margin:0 12px 3px 0;vertical-align:middle}
.intro ul.personal{margin:0 0 0 16px;line-height:15.5px}
.intro .closing{font-style:italic;font-weight:700;font-size:10.5px;margin:5px 0 0 16px}
.postage{position:absolute;left:515px;top:169px;width:107px;height:107px;border:1px solid #b9bcbf;display:flex;align-items:center;justify-content:center;font-family:"Quicksand",sans-serif;font-weight:600;font-size:11px;color:var(--grey)}
.sender{position:absolute;left:406px;top:300px;font-family:"Quicksand",sans-serif;font-style:normal;font-weight:600;font-size:9.6px;line-height:11.6px;color:var(--grey);white-space:nowrap}
.addressee{position:absolute;left:406px;top:384px;font-family:"Quicksand",sans-serif;font-weight:600;font-size:9.6px;color:var(--grey)}
</style>
</head>
<body>

<section class="card card-front">
  <svg class="front-art" viewBox="0 0 644 482" width="644" height="482">
    <defs>
      <path id="arc1" d="M119 274 A46 46 0 1 1 185 274"/>
      <path id="arc2" d="M234 274 A46 46 0 1 1 300 274"/>
      <path id="arc3" d="M357 274 A46 46 0 1 1 423 274"/>
      <path id="arc4" d="M469 274 A46 46 0 1 1 535 274"/>
    </defs>
    <path d="M0 250 C160 230 330 205 644 170 V482 H0 Z" fill="#1e7ccb" opacity=".55"/>
    <path d="M0 275 C180 250 360 220 644 195 V482 H0 Z" fill="#1a74c2"/>
    <g fill="#1d7fcd" stroke="#3aa4ec" stroke-width="3">
      <circle cx="152" cy="241" r="52"/><circle cx="267" cy="241" r="52"/>
      <circle cx="390" cy="241" r="52"/><circle cx="502" cy="241" r="52"/>
    </g>
    <g fill="#0f3e66">
      <circle cx="152" cy="241" r="37" role="img" aria-label="Icon: helper with a wheelchair user"/>
      <circle cx="267" cy="241" r="37" role="img" aria-label="Icon: judge's gavel"/>
      <circle cx="390" cy="241" r="37" role="img" aria-label="Icon: three people linked by arrows"/>
      <circle cx="502" cy="241" r="37" role="img" aria-label="Icon: laptop with network symbol"/>
    </g>
    <g font-family="Quicksand, sans-serif" font-size="6.6" font-weight="600" fill="#ffffff">
      <text><textPath href="#arc1" startOffset="12%">helping disabled people</textPath></text>
      <text><textPath href="#arc2" startOffset="3%">we understand the us social security legal systems</textPath></text>
      <text><textPath href="#arc3" startOffset="0%">we have a process to provide you leads that meet your criteria</textPath></text>
      <text><textPath href="#arc4" startOffset="2%">we have great technology that connects people</textPath></text>
    </g>
  </svg>

  <div class="brand">QUIK PATH PROSPECTS</div>

  <div class="pill" style="left:42px;top:315px;width:272px">
    <span class="pill-icon" role="img" aria-label="Icon: person with money bag"></span>
    <h3>Best Leads, Best Price</h3>
    <ul><li>High conversation rates</li><li>Referrals available</li></ul>
  </div>
  <div class="pill" style="left:336px;top:320px;width:272px">
    <span class="pill-icon" role="img" aria-label="Icon: handshake"></span>
    <h3>Trusted Partner</h3>
    <ul><li>Reliability, dependable, helpful</li><li>Deep business &amp; process acumen</li></ul>
  </div>
  <div class="pill" style="left:42px;top:392px;width:272px">
    <span class="pill-icon" role="img" aria-label="Icon: person beside a bar chart"></span>
    <h3>High Volume, Quality Leads</h3>
    <ul><li>Tested technology</li><li>50 years of SSD domain knowledge</li></ul>
  </div>
  <div class="pill" style="left:336px;top:395px;width:272px">
    <span class="pill-icon pill-mark">QUIK PATH</span>
    <h3>EZ to use</h3>
    <ul><li>We integrate seamlessly</li><li>If it is not right, we will fix it</li></ul>
  </div>
</section>

<section class="card card-back">
  <svg class="back-art" viewBox="0 0 644 488" width="644" height="488">
    <defs>
      <linearGradient id="band" x1="0" y1="0" x2="1" y2="0">
        <stop offset="0" stop-color="#1466ae"/><stop offset="1" stop-color="#0b2f4e"/>
      </linearGradient>
    </defs>
    <rect width="644" height="126" fill="url(#band)"/>
    <path d="M0 0 H130 C95 60 70 110 55 170 C42 240 36 360 34 488 H0 Z" fill="#0f4d84"/>
    <path d="M0 126 H160 C115 148 88 180 76 230 C66 280 60 380 58 488 H0 Z" fill="#1a74c2"/>
    <path d="M130 0 H146 C100 70 70 140 58 230 C50 300 46 400 46 488 H38 C38 400 42 300 50 230 C62 140 92 70 130 0 Z" fill="#3aa0e8" opacity=".7"/>
    <circle cx="87" cy="96" r="66" fill="#2d95e0"/>
    <circle cx="87" cy="96" r="58" fill="#8a9bab" role="img" aria-label="Portrait photo of Marcus Delane"/>
  </svg>

  <div class="back-name">Marcus Delane</div>
  <div class="back-role">President, Quik Path Prospects</div>
  <div class="back-brand">QUIK PATH<br>PROSPECTS</div>

  <p class="tagline">Best Leads … Best Price with High Volume &amp; Quality capacity …<br>Leads from a Trusted Partner that is EZ to use</p>

  <div class="copy test">
    <h2>Test our Leads</h2>
    <ul><li>250, 500, or even 1000 monthly leads.</li><li>Together we will find the right solution.</li></ul>
  </div>

  <div class="copy intro">
    <h4>I want to personally introduce our company to you!</h4>
    <ul>
      <li>My team has over 50 years of SSD / I experience.</li>
      <li>We have proven lead generation technology.</li>
      <li>We are EZ to work with … my team and I are always available.</li>
      <li>Our business &amp; technical acumen is unrivaled.</li>
    </ul>
    <h5>Me Personally:</h5>
    <ul class="personal">
      <li>I came out of retirement from Kelvo to make this happen.</li>
      <li>My passion is building businesses.</li>
      <li>My vision is a long term partnership with every customer.</li>
    </ul>
    <p class="closing">Let’s bring SSD/I benefits to those in need and deserving!</p>
  </div>

  <div class="postage">Postage</div>
  <address class="sender">
    Marcus Delane, President Quik Path Prospects<br>
    4120 Riverside Avenue, Suite 300<br>
    Dayton Ohio OH 45402<br>
    555-014-2271<br>
    marcus@quikpathprospects.com
  </address>
  <div class="addressee">To: Addressee</div>
</section>

</body>
</html>
```